Apple Cider

We currently export our wine throughout Asia and China, now our intention is to enter the younger 18+ age market with an Alcoholic Cider using our brand name THE LARK HOLLOW.
The Cider is in a 330 ml bottle in a Green colour and packed in clusters of 6 into a carton of 24.
The closure will be a crown twist top or Stelvin cap. Probably Red in colour
The younger market consumer has a high female content and students who need a fun and interesting label, maybe even a little risque. this market uses the product a lot as a takeaway in satchels and handbags
All wording to be in English
This is only for a bottle label
The younger market is volume orientated should the label be appealing.
Updates

You can see by our website that we have wine which is distributed throughout Asia and China. The wine market seems to be made up of the 30 plus age, probably used more at on license premises. Therefore we are not catering for the younger market which would be 18 - 30 year od group. Interstingly this group are predominantly female then there are a mix of male and female students. They want a low acholic drink with a slight carbonated ( Fizzy ) finish. The bottle size of 330 ml with an easy open twist crown cap is important, they purchase as a drink within bars etc but a lot is consumed off premise, the small bottle allows to be put into handbags and satchels. Our selection of the name THE LARK HOLLOW we hope will appeal to this group so we are looking at fun type of label, please NO NUNS MASKS! We think the label will be in the 9 cm long - 3cm wide area, as we offer both loosepacking in cartons of 24 the bottle can esily be viewed but within a 6 pack carry pack we need to overcome the indentification probably on the top of the labelor possibly a small neck band as well. We did consider using the Nun photo of holding her finger to her lips to indicat a secret or silence

Target Market(s)

18 to 35 Asian

Font styles to use
Decorative
Script

Colors

Designer to choose colors to be used in the design.

Requirements
Must have
• We are looking for a young modern and fresh label. for the younger market, we have not settled on any colour theme so its wide open to you.
Nice to have
• While we have posted an image as a guide we would want other alternatives so as to portray a secret
Should not have
• No face masks please

```html
<!DOCTYPE html>
<html lang="en">
<head>
<meta charset="utf-8">
<title>The Lark Hollow — Cider Label</title>
<link rel="stylesheet" href="https://fonts.googleapis.com/css2?family=Cinzel:wght@400&display=swap">
<style>
  :root {
    --page: #ffffff;
    --paper: #f6f5f3;
    --speckle: #e4e2df;
    --strip: #ffffff;
    --curl: #e9e8e6;
    --brush: #e6e2e2;
    --ink: #121212;
    --accent: #b3191c;
  }
  html, body {
    margin: 0;
    padding: 0;
    width: 1200px;
    height: 1062px;
    overflow: hidden;
    background: var(--page);
  }
  .canvas {
    position: relative;
    width: 1200px;
    height: 1062px;
  }
  .label {
    position: absolute;
    left: 50px;
    top: 49px;
    width: 1100px;
    height: 964px;
    overflow: hidden;
  }
  .label__texture {
    position: absolute;
    inset: 0;
    background: radial-gradient(ellipse at center, var(--paper) 55%, var(--speckle) 100%);
  }
  .label__strip {
    position: absolute;
    left: 63px;
    top: 322px;
    width: 872px;
    height: 238px;
  }
  .label__brush {
    position: absolute;
    left: 80px;
    top: 676px;
    width: 920px;
    height: 210px;
  }
  .brand {
    position: absolute;
    margin: 0;
    font-family: "Cinzel", "Times New Roman", serif;
    font-weight: 400;
    color: var(--ink);
    line-height: 1;
    white-space: nowrap;
  }
  .brand--the {
    left: 212px;
    top: 112px;
    font-size: 218px;
  }
  .brand__mark {
    position: absolute;
    left: 736px;
    top: 148px;
    width: 124px;
    height: 124px;
    border-radius: 50%;
    background: var(--accent);
  }
  .brand--lark {
    left: 246px;
    top: 316px;
    font-size: 258px;
  }
  .brand--hollow {
    left: 112px;
    top: 700px;
    font-size: 150px;
    letter-spacing: 0.2em;
    transform: rotate(-5deg);
    transform-origin: left bottom;
  }
</style>
</head>
<body>
  <main class="canvas">
    <section class="label">
      <div class="label__texture" role="img" aria-label="Speckled grey grunge paper texture"></div>

      <svg class="label__brush" viewBox="0 0 920 210" role="img" aria-label="Soft grey brush stroke behind the bottom line">
        <defs>
          <linearGradient id="brushTone" x1="0" y1="0" x2="1" y2="0">
            <stop offset="0" stop-color="#e6e2e2" stop-opacity="0.4"/>
            <stop offset="0.3" stop-color="#e6e2e2"/>
            <stop offset="1" stop-color="#e6e2e2" stop-opacity="0.5"/>
          </linearGradient>
        </defs>
        <path d="M20 120 L900 40 L910 150 L30 200 Z" fill="url(#brushTone)"/>
      </svg>

      <svg class="label__strip" viewBox="0 0 872 238" role="img" aria-label="Torn white paper strip with a curled left edge">
        <path d="M150 10 L872 20 L860 228 L150 218 Z" fill="var(--strip)"/>
        <path d="M20 40 Q90 20 170 30 L175 218 L150 210 Q120 238 60 232 Q30 220 40 190 L30 60 Z" fill="var(--curl)"/>
      </svg>

      <p class="brand brand--the">THE</p>
      <span class="brand__mark" aria-hidden="true"></span>
      <p class="brand brand--lark">LARK</p>
      <p class="brand brand--hollow">HOLLOW</p>
    </section>
  </main>
</body>
</html>
```